Long term Care Provider Conference

Banner for LTC providers to know that they can rely on us to deliver high value, cost efficient, professional back office support to streamline operations, improve and maintain compliance with administrative and or nursing solutions for their agency.

Want to update the wording

```html
<!DOCTYPE html>
<html lang="en">
<head>
<meta charset="utf-8">
<title>Brightpath Solutions – LTC Conference Banner</title>
<link rel="stylesheet" href="https://fonts.googleapis.com/css2?family=Poppins:wght@400;500;600;700;800&display=swap">
<style>
  :root {
    --stage: #ffffff;
    --teal: #4b8d94;
    --teal-light: #6fb6bb;
    --mint: #e6f6f7;
    --ink: #2f3235;
    --charcoal: #3a3d40;
    --taupe: #cbbdb8;
    --grey-icon: #9c9c9e;
    --white: #ffffff;
  }
  * { box-sizing: border-box; margin: 0; padding: 0; }
  html, body { width: 1043px; height: 1200px; overflow: hidden; background: var(--stage); }
  body { font-family: "Poppins", sans-serif; color: var(--ink); }

  .banner {
    position: absolute; left: 0; top: 31px; width: 1043px; height: 1138px; overflow: hidden;
    background: linear-gradient(150deg, var(--mint) 0%, #f4fbfb 35%, var(--white) 60%, var(--white) 100%);
  }

  .kicker {
    position: absolute; left: 54px; top: 78px;
    font-size: 25px; font-weight: 500; letter-spacing: 0.52em; color: var(--ink);
  }
  .headline {
    position: absolute; left: 50px; top: 108px;
    font-size: 84px; line-height: 83px; font-weight: 700; color: var(--teal); letter-spacing: -1px;
  }
  .intro {
    position: absolute; left: 54px; top: 286px; width: 450px;
    font-size: 27px; line-height: 39px; font-weight: 400; color: var(--ink);
  }
  .intro strong { font-weight: 700; }

  .pill {
    position: absolute; left: 56px; width: 434px; height: 68px; border-radius: 34px;
    display: flex; align-items: center; gap: 12px; padding-left: 18px;
    font-size: 25px; font-weight: 700; color: var(--ink); background: var(--taupe);
  }
  .pill svg { width: 46px; height: 46px; flex: none; }
  .pill--staffing { top: 470px; }
  .pill--compliance { top: 552px; left: 53px; width: 447px; height: 64px; background: var(--charcoal); color: var(--white); }
  .pill--cost { top: 627px; height: 67px; }

  .logo {
    position: absolute; left: 600px; top: 92px; display: flex; align-items: center; gap: 14px;
  }
  .logo-dot { width: 62px; height: 62px; border-radius: 50%; background: var(--teal); flex: none; }
  .logo-name { font-size: 30px; font-weight: 700; color: var(--charcoal); line-height: 1.1; width: 300px; }

  .photo-accent {
    position: absolute; left: 880px; top: 180px; width: 220px; height: 260px;
    border-radius: 110px 0 0 110px; background: var(--teal); opacity: 0.9;
  }
  .photo {
    position: absolute; left: 499px; top: 218px; width: 506px; height: 506px; border-radius: 50%;
    background: radial-gradient(circle at 60% 55%, #e9e4e1 0%, #cfc9c6 40%, #6d8284 75%, #3f5a5e 100%);
  }

  .feature {
    position: absolute; left: 61px; display: flex; align-items: center; gap: 24px;
    font-size: 19px; line-height: 25px; font-weight: 500; color: var(--ink);
  }
  .feature-icon {
    width: 70px; height: 70px; border-radius: 50%; background: var(--grey-icon);
    display: flex; align-items: center; justify-content: center; flex: none;
  }
  .feature--backoffice { top: 726px; }
  .feature--nursing { top: 827px; }

  .waves {
    position: absolute; left: 0; bottom: 0; width: 1043px; height: 250px;
    background: linear-gradient(180deg, rgba(255,255,255,0) 0%, rgba(150,214,216,0.25) 60%, rgba(120,200,204,0.4) 100%);
  }

  .tagline {
    position: absolute; left: 0; width: 1043px; top: 938px; text-align: center;
    font-size: 24px; font-weight: 700; color: var(--teal);
  }
  .cta {
    position: absolute; left: 159px; top: 985px; width: 725px; height: 72px; border-radius: 36px;
    background: var(--charcoal); box-shadow: 0 10px 18px rgba(0,0,0,0.15);
    display: flex; align-items: center; justify-content: center;
    font-size: 34px; font-weight: 700; letter-spacing: 0.18em; color: var(--white);
  }
</style>
</head>
<body>
  <main class="banner">
    <p class="kicker">TRANSFORMING</p>
    <h1 class="headline">Long-Term<br>Care,</h1>
    <p class="intro"><strong>Improving quality of care</strong> while easing <strong>administrative</strong> and <strong>staffing burdens</strong> for providers</p>

    <div class="logo">
      <span class="logo-dot"></span>
      <span class="logo-name">Brightpath Solutions</span>
    </div>

    <div class="photo-accent"></div>
    <div class="photo" role="img" aria-label="Photo of a smiling support agent with a headset working at a computer in a bright office"></div>

    <div class="pill pill--staffing">
      <svg viewBox="0 0 46 46"><path d="M23 5 L37 10 V22 C37 31 30 37 23 40 C16 37 9 31 9 22 V10 Z" fill="none" stroke="#fff" stroke-width="3"/><path d="M16 22 L21 27 L30 17" fill="none" stroke="#fff" stroke-width="3.5" stroke-linecap="round" stroke-linejoin="round"/></svg>
      DEPENDABLE STAFFING
    </div>
    <div class="pill pill--compliance">
      <svg viewBox="0 0 46 46"><circle cx="23" cy="23" r="18" fill="#4b8d94"/><path d="M15 23 L21 29 L31 17" fill="none" stroke="#fff" stroke-width="3.5" stroke-linecap="round" stroke-linejoin="round"/></svg>
      COMPLIANCE-DRIVEN
    </div>
    <div class="pill pill--cost">
      <svg viewBox="0 0 46 46"><circle cx="18" cy="28" r="11" fill="none" stroke="#fff" stroke-width="3"/><path d="M18 22 V28 H23" fill="none" stroke="#fff" stroke-width="2.5" stroke-linecap="round"/><path d="M36 40 V8 M30 14 L36 8 L42 14" fill="none" stroke="#fff" stroke-width="3" stroke-linecap="round" stroke-linejoin="round"/></svg>
      COST EFFICIENT
    </div>

    <div class="feature feature--backoffice">
      <span class="feature-icon"><svg width="36" height="36" viewBox="0 0 36 36"><rect x="7" y="5" width="22" height="26" rx="3" fill="none" stroke="#fff" stroke-width="3"/><path d="M12 13 H24 M12 19 H24 M12 25 H19" stroke="#fff" stroke-width="2.5" stroke-linecap="round"/></svg></span>
      <p>Streamline operations with expert back-office support in HR,<br>Billing, and Scheduling.</p>
    </div>
    <div class="feature feature--nursing">
      <span class="feature-icon"><svg width="36" height="36" viewBox="0 0 36 36"><path d="M18 6 V30 M6 18 H30" stroke="#fff" stroke-width="7" stroke-linecap="round"/></svg></span>
      <p>Ensure compliance with reliable nursing and administrative solutions<br>tailored for LTC providers.</p>
    </div>

    <div class="waves" role="img" aria-label="Soft flowing teal line pattern along the bottom edge"></div>

    <p class="tagline">Partner with Brightpath to strengthen your healthcare team</p>
    <div class="cta">www.brightpath-ltc.com</div>
  </main>
</body>
</html>
```